a graphic model of stress response for online learning course

We need a model of how the brain experiences, interprets and responds to stressors. There are three components to this.

I need a simple linear graphic of the three stages with arrows between to show progression:
1. We experience the stressor
2. Our brain interprets the stressor: Is it a threat? Is it friendly?
3. Our brain creates the appropriate stress response: physical, mental, emotional

And another graphic with illustrations of this process:
A charging lion
A brain thinking/interpreting the potential stressor
A person running away (the response to the threat).

Needs to be used for online learning course about stress and resilience.

See attached for assistance.

```html
<!DOCTYPE html>
<html lang="en">
<head>
<meta charset="utf-8">
<title>Stress Response Model</title>
<link href="https://fonts.googleapis.com/css2?family=Montserrat:wght@600;700&display=swap" rel="stylesheet">
<style>
  :root {
    --ink: #2f2f2f;
    --paper: #ffffff;
    --bg: #fefefe;
    --orange-a: #fd9350;
    --orange-b: #f77a22;
    --grey-a: #bdbdbd;
    --grey-b: #9b9b9b;
    --yellow-a: #fdd33a;
    --yellow-b: #f4c20d;
  }
  html, body {
    margin: 0;
    padding: 0;
    width: 1200px;
    height: 1000px;
    overflow: hidden;
    background: var(--bg);
    font-family: "Montserrat", sans-serif;
  }
  .model {
    position: relative;
    width: 1200px;
    height: 1000px;
  }
  .model__shapes {
    position: absolute;
    inset: 0;
  }
  .stage-label {
    position: absolute;
    z-index: 2;
    margin: 0;
    font-weight: 700;
    font-size: 16px;
    line-height: 19px;
    color: var(--ink);
    letter-spacing: 0.1px;
  }
  .stage-label--one { left: 158px; top: 528px; }
  .stage-label--two { left: 482px; top: 527px; }
  .stage-label--three { left: 805px; top: 527px; }
  .stage-number {
    font-weight: 700;
    font-size: 32px;
    fill: var(--ink);
  }
</style>
</head>
<body>
<main class="model">
  <svg class="model__shapes" width="1200" height="1000" viewBox="0 0 1200 1000">
    <defs>
      <linearGradient id="grad-orange" x1="0" x2="1">
        <stop offset="0" stop-color="var(--orange-a)"/>
        <stop offset="1" stop-color="var(--orange-b)"/>
      </linearGradient>
      <linearGradient id="grad-grey" x1="0" x2="1">
        <stop offset="0" stop-color="var(--grey-a)"/>
        <stop offset="1" stop-color="var(--grey-b)"/>
      </linearGradient>
      <linearGradient id="grad-yellow" x1="0" x2="1">
        <stop offset="0" stop-color="var(--yellow-a)"/>
        <stop offset="1" stop-color="var(--yellow-b)"/>
      </linearGradient>
      <filter id="card-shadow" x="-20%" y="-20%" width="140%" height="140%">
        <feDropShadow dx="-6" dy="8" stdDeviation="6" flood-color="#000" flood-opacity="0.12"/>
      </filter>
    </defs>

    <!-- Stage 1 -->
    <g class="stage stage--one">
      <rect class="stage__card" x="151" y="268" width="243" height="373" rx="24" fill="var(--paper)" stroke="var(--ink)" stroke-width="2.5" filter="url(#card-shadow)"/>
      <rect class="stage__illustration" role="img" aria-label="Silhouette of a charging lion" x="166" y="362" width="214" height="144" rx="14" fill="var(--ink)"/>
      <path class="stage__band-fold" d="M133 506 L133 498 Q140 494 151 492 L151 506 Z" fill="var(--orange-a)" stroke="var(--ink)" stroke-width="2"/>
      <path class="stage__band" d="M133 506 H369 A50.5 50.5 0 0 1 369 607 H133 Z" fill="url(#grad-orange)" stroke="var(--ink)" stroke-width="2.5"/>
      <circle class="stage__badge" cx="215" cy="283" r="31" fill="url(#grad-orange)" stroke="var(--ink)" stroke-width="2.5"/>
      <text class="stage-number" x="215" y="295" text-anchor="middle">01</text>
      <path class="stage__arrow" d="M394 641 H436" stroke="var(--ink)" stroke-width="2.5" fill="none"/>
      <path class="stage__arrowhead" d="M433 629 L455 641 L433 653 Z" fill="var(--ink)"/>
    </g>

    <!-- Stage 2 -->
    <g class="stage stage--two">
      <rect class="stage__card" x="475" y="268" width="243" height="373" rx="24" fill="var(--paper)" stroke="var(--ink)" stroke-width="2.5" filter="url(#card-shadow)"/>
      <rect class="stage__illustration" role="img" aria-label="Head in profile with a brain and a question mark" x="526" y="350" width="140" height="156" rx="40" fill="var(--ink)"/>
      <path class="stage__band-fold" d="M457 506 L457 498 Q464 494 475 492 L475 506 Z" fill="var(--grey-a)" stroke="var(--ink)" stroke-width="2"/>
      <path class="stage__band" d="M457 506 H693 A50.5 50.5 0 0 1 693 607 H457 Z" fill="url(#grad-grey)" stroke="var(--ink)" stroke-width="2.5"/>
      <circle class="stage__badge" cx="533" cy="283" r="31" fill="url(#grad-grey)" stroke="var(--ink)" stroke-width="2.5"/>
      <text class="stage-number" x="533" y="295" text-anchor="middle">02</text>
      <path class="stage__arrow" d="M718 641 H760" stroke="var(--ink)" stroke-width="2.5" fill="none"/>
      <path class="stage__arrowhead" d="M757 629 L779 641 L757 653 Z" fill="var(--ink)"/>
    </g>

    <!-- Stage 3 -->
    <g class="stage stage--three">
      <rect class="stage__card" x="800" y="268" width="243" height="373" rx="24" fill="var(--paper)" stroke="var(--ink)" stroke-width="2.5" filter="url(#card-shadow)"/>
      <rect class="stage__illustration" role="img" aria-label="Silhouette of a person running away" x="883" y="320" width="131" height="186" rx="16" fill="var(--ink)"/>
      <path class="stage__band-fold" d="M782 506 L782 498 Q789 494 800 492 L800 506 Z" fill="var(--yellow-a)" stroke="var(--ink)" stroke-width="2"/>
      <path class="stage__band" d="M782 506 H1018 A50.5 50.5 0 0 1 1018 607 H782 Z" fill="url(#grad-yellow)" stroke="var(--ink)" stroke-width="2.5"/>
      <circle class="stage__badge" cx="858" cy="283" r="31" fill="url(#grad-yellow)" stroke="var(--ink)" stroke-width="2.5"/>
      <text class="stage-number" x="858" y="295" text-anchor="middle">03</text>
    </g>
  </svg>

  <p class="stage-label stage-label--one">We experience<br>the stressor</p>
  <p class="stage-label stage-label--two">Our brain interprets<br>the stressor:<br>Is it a threat? Is it friendly?</p>
  <p class="stage-label stage-label--three">Our brain creates the<br>appropriate stress response:<br>physical, mental, emotional</p>
</main>
</body>
</html>
```